App-Design für IT-Sicherheitsfirma
Zielgruppe
Wir sind eine IT-Sicherheitsfirma und suchen ein funktionelles und schlankes App Design.
Unsere Nutzer sind Mitarbeiter von international agierenden Konzernen. Die Zielgruppe sind international agierende Konzerne.
Die App gibt die Möglichkeit zu einem sehr sicheren Login auf Großrechner (Mainframes) via Handy oder Webinterface. Vereinfacht gesagt ist sie ein Login-Tool, Schlüssel oder Authenticator.
Aufgabenstellung
Die App soll übersichtlich, sicher, modern, schlicht und smart aussehen. Schön aber kein muss wäre die Verwendung von Elementen aus 'wirbel/gestalt' da wir die App auf dieser Plattform programmieren wollen.
https://gestaltkern.io/design/gestalt-theming/overview.html#gestalt-theming
https://wirbel.dev/docs/development/ui/widgets/gestalt

```html
<!DOCTYPE html>
<html lang="de">
<head>
<meta charset="utf-8">
<title>Velqor App Screens</title>
<link href="https://fonts.googleapis.com/css2?family=Roboto:wght@400;500;700&display=swap" rel="stylesheet">
<style>
:root{
  --canvas:#b3b3b3;
  --brand-red:#c8102e;
  --black:#000;
  --white:#fff;
}
*{box-sizing:border-box;margin:0;padding:0}
html,body{width:1200px;height:2721px;overflow:hidden;background:var(--canvas);font-family:'Roboto',sans-serif}
.board{position:relative;width:1136px;height:2576px;transform:scale(1.0563);transform-origin:0 0}
.phone{position:absolute;width:350px;height:739px;overflow:hidden;background:var(--bg);color:var(--text)}
.dark{--bg:#000;--bg-top:#222;--text:#fff;--muted:#8a8a8a;--card:#141414;--field:#111;--field-line:#999;--outline:#fff;--tab-bar:#111;--tab-idle:#fff;--card-border:#555}
.light{--bg:#ececec;--bg-top:#f8f8f8;--text:#1a1a1a;--muted:#8a8a8a;--card:#fff;--field:#f6f6f6;--field-line:#b5b5b5;--outline:#1a1a1a;--tab-bar:#fafafa;--tab-idle:#888;--card-border:transparent}
.light.welcome{--bg:#fff}
.backdrop{position:absolute;inset:0;background:linear-gradient(160deg,var(--bg-top) 0%,var(--bg) 60%)}
.status{position:absolute;top:6px;right:18px;display:flex;gap:4px;align-items:center;opacity:.5}
.status i{display:block;width:7px;height:7px;background:var(--muted)}
.status i.dot{border-radius:50%}
.status i.tri{background:none;width:0;height:0;border-left:5px solid transparent;border-right:5px solid transparent;border-top:7px solid var(--muted)}
.navbar{position:absolute;left:0;right:0;bottom:0;height:40px;background:#000;display:flex;justify-content:space-around;align-items:center;padding:0 60px}
.navbar svg{width:14px;height:14px}
.wordmark{position:absolute;top:55px;right:22px;display:flex;align-items:center;gap:6px;font-weight:700;font-size:20px;color:var(--text)}
.wordmark i{display:block;width:10px;height:10px;border-radius:50%;background:var(--brand-red)}
.hero{position:absolute;left:21px;top:225px;font-size:40px;line-height:48px;font-weight:700}
.lead{position:absolute;left:21px;top:388px;font-size:20px;line-height:25px}
.btn{position:absolute;left:20px;width:310px;height:33px;border-radius:3px;font-size:11px;font-weight:500;letter-spacing:1.3px;display:flex;align-items:center;justify-content:center;text-transform:uppercase}
.btn-primary{background:var(--brand-red);color:#fff}
.btn-outline{border:1.5px solid var(--outline);color:var(--text)}
.appbar{position:absolute;left:0;right:0;top:32px;height:26px;display:flex;align-items:center;font-size:17px;font-weight:500}
.appbar .back{position:absolute;left:20px}
.appbar .title{position:absolute;left:70px}
.appbar .plain{position:absolute;left:21px}
.appbar .gear{position:absolute;right:20px}
.page-title{position:absolute;left:21px;font-size:28px;line-height:31px;font-weight:700}
.section{position:absolute;left:21px;font-size:13px;font-weight:700}
.device-card{position:absolute;left:20px;top:211px;width:310px;height:97px;background:var(--card);border-radius:3px}
.device-card svg{position:absolute;left:18px;top:30px}
.spec{position:absolute;left:65px;font-size:13px;display:grid;grid-template-columns:75px auto;row-gap:9px;top:15px}
.spec dt{color:var(--muted)}
.field{position:absolute;height:48px;background:var(--field);border-bottom:1.5px solid var(--field-line);font-size:13px;padding:0 14px;display:flex;align-items:center;justify-content:space-between;color:var(--text)}
.light .field{color:#777}
.hint{position:absolute;left:21px;top:552px;width:290px;font-size:9px;line-height:13.5px;color:var(--text)}
.light .hint{color:#777}
.frame-card{position:absolute;left:20px;width:310px;height:93px;background:var(--card);border:1px solid var(--card-border);border-radius:3px}
.frame-card .user{position:absolute;left:17px;top:14px;font-size:13px;font-weight:700}
.frame-card .name{position:absolute;left:17px;top:40px;font-size:13.5px}
.frame-card .host{position:absolute;left:17px;top:62px;font-size:13.5px;color:var(--muted)}
.frame-card svg{position:absolute;right:15px;top:38px}
.tabbar{position:absolute;left:0;right:0;top:650px;height:48px;background:var(--tab-bar);display:flex}
.tab{flex:1;display:flex;flex-direction:column;align-items:center;justify-content:center;gap:3px;font-size:9px;color:var(--tab-idle)}
.tab.active{color:var(--brand-red)}
</style>
</head>
<body>
<main class="board">

  <!-- Welcome, dark -->
  <section class="phone dark welcome" style="left:156px;top:90px">
    <div class="backdrop" role="img" aria-label="Dunkles, facettiertes Polygonmuster als Hintergrund"></div>
    <div class="status"><i></i><i class="dot"></i><i class="tri"></i></div>
    <div class="wordmark">Velqor<i></i></div>
    <h1 class="hero">Velqor –<br>the digital<br>security experts</h1>
    <p class="lead">Lorem ipsum dolor sit amet,<br>consectetuer adipiscing elit.</p>
    <div class="btn btn-primary" style="top:466px">Registrieren</div>
    <div class="btn btn-outline" style="top:511px">Login</div>
    <nav class="navbar">
      <svg viewBox="0 0 14 14"><path d="M11 2 3 7l8 5z" fill="none" stroke="#fff" stroke-width="1.5"/></svg>
      <svg viewBox="0 0 14 14"><circle cx="7" cy="7" r="5.5" fill="none" stroke="#fff" stroke-width="1.5"/></svg>
      <svg viewBox="0 0 14 14"><rect x="2" y="2" width="10" height="10" fill="none" stroke="#fff" stroke-width="1.5"/></svg>
    </nav>
  </section>

  <!-- Welcome, light -->
  <section class="phone light welcome" style="left:624px;top:90px;height:735px">
    <div class="backdrop" role="img" aria-label="Helles, facettiertes Polygonmuster als Hintergrund"></div>
    <div class="status"><i></i><i class="dot"></i><i class="tri"></i></div>
    <div class="wordmark">Velqor<i></i></div>
    <h1 class="hero" style="top:223px">Velqor –<br>the digital<br>security experts</h1>
    <p class="lead" style="top:386px">Lorem ipsum dolor sit amet,<br>consectetuer adipiscing elit.</p>
    <div class="btn btn-primary" style="top:463px">Registrieren</div>
    <div class="btn btn-outline" style="top:508px">Login</div>
    <nav class="navbar">
      <svg viewBox="0 0 14 14"><path d="M11 2 3 7l8 5z" fill="none" stroke="#fff" stroke-width="1.5"/></svg>
      <svg viewBox="0 0 14 14"><circle cx="7" cy="7" r="5.5" fill="none" stroke="#fff" stroke-width="1.5"/></svg>
      <svg viewBox="0 0 14 14"><rect x="2" y="2" width="10" height="10" fill="none" stroke="#fff" stroke-width="1.5"/></svg>
    </nav>
  </section>

  <!-- Registration, dark -->
  <section class="phone dark" style="left:156px;top:911px">
    <div class="backdrop" role="img" aria-label="Dunkles, facettiertes Polygonmuster als Hintergrund"></div>
    <div class="status"><i></i><i class="dot"></i><i class="tri"></i></div>
    <header class="appbar">
      <svg class="back" width="8" height="12" viewBox="0 0 8 12"><path d="M6 1 1.5 6 6 11" fill="none" stroke="currentColor" stroke-width="1.8"/></svg>
      <span class="title">Registrierung</span>
    </header>
    <h2 class="page-title" style="top:97px">Mit E-Mailadresse<br>registrieren</h2>
    <h3 class="section" style="top:188px">Dein Device</h3>
    <div class="device-card">
      <svg width="24" height="36" viewBox="0 0 24 36"><rect x="2" y="2" width="20" height="32" rx="3" fill="none" stroke="currentColor" stroke-width="3"/></svg>
      <dl class="spec"><dt>NAME</dt><dd>Pixa 7</dd><dt>MODEL</dt><dd>Orchard Phone</dd><dt>OS</dt><dd>PhoneOS 14.6</dd></dl>
    </div>
    <h3 class="section" style="top:341px">Deine Zugangsdaten</h3>
    <div class="field" style="left:20px;top:370px;width:310px">E-Mailadresse</div>
    <div class="field" style="left:20px;top:432px;width:151px">Vorname</div>
    <div class="field" style="left:179px;top:432px;width:151px">Nachname</div>
    <div class="field" style="left:20px;top:494px;width:310px">Passwort
      <svg width="18" height="12" viewBox="0 0 18 12"><path d="M1 6c2-3.5 5-5 8-5s6 1.5 8 5c-2 3.5-5 5-8 5S3 9.5 1 6z" fill="currentColor"/><circle cx="9" cy="6" r="2.6" fill="var(--field)"/></svg>
    </div>
    <p class="hint">Dein Passwort muss aus mindestens 8 Zeichen bestehen und einen Großbuchstaben, eine Zahl und ein Sonderzeichen umfassen.</p>
    <div class="btn btn-primary" style="top:627px">Jetzt registrieren</div>
    <nav class="navbar">
      <svg viewBox="0 0 14 14"><path d="M11 2 3 7l8 5z" fill="none" stroke="#fff" stroke-width="1.5"/></svg>
      <svg viewBox="0 0 14 14"><circle cx="7" cy="7" r="5.5" fill="none" stroke="#fff" stroke-width="1.5"/></svg>
      <svg viewBox="0 0 14 14"><rect x="2" y="2" width="10" height="10" fill="none" stroke="#fff" stroke-width="1.5"/></svg>
    </nav>
  </section>

  <!-- Registration, light -->
  <section class="phone light" style="left:624px;top:911px;height:735px">
    <div class="backdrop" role="img" aria-label="Helles, facettiertes Polygonmuster als Hintergrund"></div>
    <div class="status"><i></i><i class="dot"></i><i class="tri"></i></div>
    <header class="appbar">
      <svg class="back" width="8" height="12" viewBox="0 0 8 12"><path d="M6 1 1.5 6 6 11" fill="none" stroke="currentColor" stroke-width="1.8"/></svg>
      <span class="title">Registrierung</span>
    </header>
    <h2 class="page-title" style="top:96px">Mit E-Mailadresse<br>registrieren</h2>
    <h3 class="section" style="top:187px">Dein Device</h3>
    <div class="device-card">
      <svg width="24" height="36" viewBox="0 0 24 36"><rect x="2" y="2" width="20" height="32" rx="3" fill="none" stroke="currentColor" stroke-width="3"/></svg>
      <dl class="spec"><dt>NAME</dt><dd>Pixa 7</dd><dt>MODEL</dt><dd>Orchard Phone</dd><dt>OS</dt><dd>PhoneOS 14.6</dd></dl>
    </div>
    <h3 class="section" style="top:339px">Deine Zugangsdaten</h3>
    <div class="field" style="left:20px;top:367px;width:310px">E-Mailadresse</div>
    <div class="field" style="left:20px;top:429px;width:151px">Vorname</div>
    <div class="field" style="left:179px;top:429px;width:151px">Nachname</div>
    <div class="field" style="left:20px;top:491px;width:310px">Passwort
      <svg width="18" height="12" viewBox="0 0 18 12"><path d="M1 6c2-3.5 5-5 8-5s6 1.5 8 5c-2 3.5-5 5-8 5S3 9.5 1 6z" fill="#555"/><circle cx="9" cy="6" r="2.6" fill="var(--field)"/></svg>
    </div>
    <p class="hint" style="top:549px">Dein Passwort muss aus mindestens 8 Zeichen bestehen und einen Großbuchstaben, eine Zahl und ein Sonderzeichen umfassen.</p>
    <div class="btn btn-primary" style="top:624px">Jetzt registrieren</div>
    <nav class="navbar">
      <svg viewBox="0 0 14 14"><path d="M11 2 3 7l8 5z" fill="none" stroke="#fff" stroke-width="1.5"/></svg>
      <svg viewBox="0 0 14 14"><circle cx="7" cy="7" r="5.5" fill="none" stroke="#fff" stroke-width="1.5"/></svg>
      <svg viewBox="0 0 14 14"><rect x="2" y="2" width="10" height="10" fill="none" stroke="#fff" stroke-width="1.5"/></svg>
    </nav>
  </section>

  <!-- Mainframe list, dark -->
  <section class="phone dark" style="left:156px;top:1749px">
    <div class="backdrop" role="img" aria-label="Dunkles, facettiertes Polygonmuster als Hintergrund"></div>
    <div class="status"><i></i><i class="dot"></i><i class="tri"></i></div>
    <header class="appbar">
      <span class="plain">Harbor Pass</span>
      <svg class="gear" width="18" height="18" viewBox="0 0 24 24"><path fill="currentColor" d="M19.4 13a7.5 7.5 0 0 0 0-2l2.1-1.6-2-3.5-2.5 1a7 7 0 0 0-1.7-1L15 3h-4l-.3 2.9a7 7 0 0 0-1.7 1l-2.5-1-2 3.5L6.6 11a7.5 7.5 0 0 0 0 2l-2.1 1.6 2 3.5 2.5-1a7 7 0 0 0 1.7 1L11 21h4l.3-2.9a7 7 0 0 0 1.7-1l2.5 1 2-3.5zM13 15.5a3.5 3.5 0 1 1 0-7 3.5 3.5 0 0 1 0 7z" transform="translate(-1 0)"/></svg>
    </header>
    <h2 class="page-title" style="top:82px">Wähle einen<br>Mainframe aus</h2>
    <article class="frame-card" style="top:165px"><span class="user">tso</span><span class="name">Velqor Demo</span><span class="host">mainframe-dev.velqor.com</span>
      <svg width="18" height="16" viewBox="0 0 18 16"><path d="M11 1h5v14h-5M1 8h10M7 4l4 4-4 4" fill="none" stroke="currentColor" stroke-width="1.6"/></svg></article>
    <article class="frame-card" style="top:271px"><span class="user">tso</span><span class="name">Velqor Demo</span><span class="host">mainframe-dev.velqor.com</span>
      <svg width="18" height="16" viewBox="0 0 18 16"><path d="M11 1h5v14h-5M1 8h10M7 4l4 4-4 4" fill="none" stroke="currentColor" stroke-width="1.6"/></svg></article>
    <article class="frame-card" style="top:377px"><span class="user">tso</span><span class="name">Velqor Demo</span><span class="host">mainframe-dev.velqor.com</span>
      <svg width="18" height="16" viewBox="0 0 18 16"><path d="M11 1h5v14h-5M1 8h10M7 4l4 4-4 4" fill="none" stroke="currentColor" stroke-width="1.6"/></svg></article>
    <div class="tabbar">
      <div class="tab active"><svg width="14" height="16" viewBox="0 0 14 16"><rect x="1" y="1" width="12" height="14" rx="1.5" fill="currentColor"/><path d="M4 5h6M4 8h6M4 11h4" stroke="var(--tab-bar)" stroke-width="1.4"/></svg>Terminal</div>
      <div class="tab"><svg width="16" height="16" viewBox="0 0 16 16"><path d="M3 8a5.5 5.5 0 1 0 1.6-3.9M4.6 4.1V1.6M4.6 4.1H2.2M8 5v3.3l2.2 1.4" fill="none" stroke="currentColor" stroke-width="1.4"/></svg>Logins</div>
    </div>
    <nav class="navbar">
      <svg viewBox="0 0 14 14"><path d="M11 2 3 7l8 5z" fill="none" stroke="#fff" stroke-width="1.5"/></svg>
      <svg viewBox="0 0 14 14"><circle cx="7" cy="7" r="5.5" fill="none" stroke="#fff" stroke-width="1.5"/></svg>
      <svg viewBox="0 0 14 14"><rect x="2" y="2" width="10" height="10" fill="none" stroke="#fff" stroke-width="1.5"/></svg>
    </nav>
  </section>

  <!-- Mainframe list, light -->
  <section class="phone light" style="left:624px;top:1749px;height:736px">
    <div class="backdrop" role="img" aria-label="Helles, facettiertes Polygonmuster als Hintergrund"></div>
    <div class="status"><i></i><i class="dot"></i><i class="tri"></i></div>
    <header class="appbar">
      <span class="plain">Harbor Pass</span>
      <svg class="gear" width="18" height="18" viewBox="0 0 24 24"><path fill="currentColor" d="M19.4 13a7.5 7.5 0 0 0 0-2l2.1-1.6-2-3.5-2.5 1a7 7 0 0 0-1.7-1L15 3h-4l-.3 2.9a7 7 0 0 0-1.7 1l-2.5-1-2 3.5L6.6 11a7.5 7.5 0 0 0 0 2l-2.1 1.6 2 3.5 2.5-1a7 7 0 0 0 1.7 1L11 21h4l.3-2.9a7 7 0 0 0 1.7-1l2.5 1 2-3.5zM13 15.5a3.5 3.5 0 1 1 0-7 3.5 3.5 0 0 1 0 7z" transform="translate(-1 0)"/></svg>
    </header>
    <h2 class="page-title" style="top:82px">Wähle einen<br>Mainframe aus</h2>
    <article class="frame-card" style="top:165px"><span class="user">tso</span><span class="name">Velqor Demo</span><span class="host">mainframe-dev.velqor.com</span>
      <svg width="18" height="16" viewBox="0 0 18 16"><path d="M11 1h5v14h-5M1 8h10M7 4l4 4-4 4" fill="none" stroke="currentColor" stroke-width="1.6"/></svg></article>
    <article class="frame-card" style="top:271px"><span class="user">tso</span><span class="name">Velqor Demo</span><span class="host">mainframe-dev.velqor.com</span>
      <svg width="18" height="16" viewBox="0 0 18 16"><path d="M11 1h5v14h-5M1 8h10M7 4l4 4-4 4" fill="none" stroke="currentColor" stroke-width="1.6"/></svg></article>
    <article class="frame-card" style="top:377px"><span class="user">tso</span><span class="name">Velqor Demo</span><span class="host">mainframe-dev.velqor.com</span>
      <svg width="18" height="16" viewBox="0 0 18 16"><path d="M11 1h5v14h-5M1 8h10M7 4l4 4-4 4" fill="none" stroke="currentColor" stroke-width="1.6"/></svg></article>
    <div class="tabbar" style="top:647px">
      <div class="tab active"><svg width="14" height="16" viewBox="0 0 14 16"><rect x="1" y="1" width="12" height="14" rx="1.5" fill="currentColor"/><path d="M4 5h6M4 8h6M4 11h4" stroke="var(--tab-bar)" stroke-width="1.4"/></svg>Terminal</div>
      <div class="tab"><svg width="16" height="16" viewBox="0 0 16 16"><path d="M3 8a5.5 5.5 0 1 0 1.6-3.9M4.6 4.1V1.6M4.6 4.1H2.2M8 5v3.3l2.2 1.4" fill="none" stroke="currentColor" stroke-width="1.4"/></svg>Logins</div>
    </div>
    <nav class="navbar">
      <svg viewBox="0 0 14 14"><path d="M11 2 3 7l8 5z" fill="none" stroke="#fff" stroke-width="1.5"/></svg>
      <svg viewBox="0 0 14 14"><circle cx="7" cy="7" r="5.5" fill="none" stroke="#fff" stroke-width="1.5"/></svg>
      <svg viewBox="0 0 14 14"><rect x="2" y="2" width="10" height="10" fill="none" stroke="#fff" stroke-width="1.5"/></svg>
    </nav>
  </section>

</main>
</body>
</html>
```